Business Card Design for Ferncliff Studios

Design the layout for a two-sided business card incorporating the logo design produced through Pixel Guild by moretundel earlier this year. Design to be created as per specifications for standard size cards produced by Kipt.com. Art work dimensions to be restricted to 3.66" x 2.16"

Front of card to include Ferncliff Studios Logo and name and contact information. Back side to include logo only.

Target Market(s)

Photography clients.

Industry/Entity Type

Business

Contact Information for Business Card

Derek Pahlmann, Photographer
23-815 Otter Bend Drive
Yellowknife, NT X0E 7K2

867-555-3816

derek@ferncliffstudios.example

www.ferncliffstudios.example

Font styles to use
Serif

Requirements
Must have
• Logo, name, contact information, email and website.
• Use colours from original logo design.
Nice to have
• I'm thinking a black background, but I'm open to other ideas.

```html
<!DOCTYPE html>
<html lang="en">
<head>
<meta charset="utf-8">
<title>Ferncliff Studios – Business Card</title>
<link rel="stylesheet" href="https://fonts.googleapis.com/css2?family=Questrial&display=swap">
<style>
  :root {
    --backdrop: #eeeeee;
    --card-black: #1e1b1d;
    --gold: #d6b468;
    --teal-light: #6fd0cc;
    --teal-mid: #4fb9c3;
    --teal-deep: #137e9c;
    --white: #ffffff;
    --ink: #1c2230;
  }
  * { margin: 0; padding: 0; box-sizing: border-box; }
  html, body {
    width: 1029px;
    height: 1200px;
    overflow: hidden;
    background: var(--backdrop);
    font-family: "Questrial", sans-serif;
  }
  .canvas {
    position: relative;
    width: 1029px;
    height: 1200px;
  }
  .card {
    position: absolute;
    left: 133px;
    width: 763px;
    height: 437px;
    background: var(--card-black);
    overflow: hidden;
  }
  .card--front { top: 135px; }
  .card--back { top: 628px; }

  .card__panel {
    position: absolute;
    inset: 0;
    background: radial-gradient(circle at 70% 75%, var(--teal-light) 0%, var(--teal-mid) 40%, var(--teal-deep) 100%);
    clip-path: polygon(0 390px, 763px 60px, 763px 437px, 0 437px);
  }

  .brand {
    position: absolute;
    display: flex;
    align-items: center;
  }
  .brand__dot {
    border: 3px solid var(--white);
    border-radius: 50%;
    flex: none;
  }
  .brand__name {
    color: var(--gold);
    font-family: "Questrial", sans-serif;
    text-transform: uppercase;
    line-height: 1;
  }
  .brand__line { display: block; }

  .card--front .brand { left: 33px; top: 26px; }
  .card--front .brand__dot { width: 88px; height: 88px; margin-right: 16px; }
  .card--front .brand__line--main { font-size: 38px; letter-spacing: 2px; }
  .card--front .brand__line--sub { font-size: 14px; letter-spacing: 9px; margin-top: 6px; padding-left: 60px; }

  .card--back .brand { left: 148px; top: 159px; }
  .card--back .brand__dot { width: 116px; height: 116px; margin-right: 20px; }
  .card--back .brand__line--main { font-size: 50px; letter-spacing: 3px; }
  .card--back .brand__line--sub { font-size: 18px; letter-spacing: 12px; margin-top: 8px; padding-left: 80px; }

  .person {
    position: absolute;
    left: 41px;
    top: 204px;
    color: var(--white);
  }
  .person__name { font-size: 29px; line-height: 1.1; }
  .person__role { font-size: 17px; line-height: 1.3; }

  .contact {
    position: absolute;
    left: 474px;
    top: 270px;
    list-style: none;
    color: var(--ink);
    font-size: 18px;
    line-height: 23.5px;
  }
  .website {
    position: absolute;
    left: 0;
    width: 763px;
    top: 395px;
    padding-left: 40px;
    text-align: center;
    color: var(--ink);
    font-weight: bold;
    font-size: 17px;
  }
</style>
</head>
<body>
<div class="canvas">

  <section class="card card--front" aria-label="Business card front">
    <div class="card__panel" role="img" aria-label="Soft teal gradient panel across the lower right of the card"></div>

    <div class="brand">
      <span class="brand__dot" aria-hidden="true"></span>
      <span class="brand__name">
        <span class="brand__line brand__line--main">Ferncliff</span>
        <span class="brand__line brand__line--sub">Studios</span>
      </span>
    </div>

    <div class="person">
      <p class="person__name">Derek Pahlmann</p>
      <p class="person__role">Photographer</p>
    </div>

    <ul class="contact">
      <li>23-815 Otter Bend Drive</li>
      <li>Yellowknife, NT X0E 7K2</li>
      <li>867-555-3816</li>
      <li>derek@ferncliffstudios.example</li>
    </ul>

    <p class="website">www.ferncliffstudios.example</p>
  </section>

  <section class="card card--back" aria-label="Business card back">
    <div class="brand">
      <span class="brand__dot" aria-hidden="true"></span>
      <span class="brand__name">
        <span class="brand__line brand__line--main">Ferncliff</span>
        <span class="brand__line brand__line--sub">Studios</span>
      </span>
    </div>
  </section>

</div>
</body>
</html>
```